Business card design for Plumbing and Gas fitting company

We need a business card design for our plumbing and gas fitting company using the company logo and director details. Design should be modern and eye-catching however kept reasonably simple. This design should be targeted at commercial businesses/work so professionalism is key.

Target Market(s)

Commercial/business

Industry/Entity Type

Plumbing

Contact Information for Business Card

Warren Dohey
Director
027 581 9043
warren@vantorplumbingandgas.example
PO Box 7816
Palmerston North 4472

Font styles to use
Sans Serif

Requirements
Must have
• Logo
• Modern
• Kept simple
Nice to have
• Colour scheme based around logo

```html
<!DOCTYPE html>
<html lang="en">
<head>
<meta charset="utf-8">
<title>Vantor Plumbing &amp; Gas – Business Card</title>
<link href="https://fonts.googleapis.com/css2?family=Open+Sans:wght@400;600&display=swap" rel="stylesheet">
<style>
  :root {
    --page-bg: #e4e6ea;
    --card-bg: #ffffff;
    --brand-blue: #1f6fc0;
    --brand-orange: #ec7a2c;
    --text-grey: #7a7a7a;
    --rule-grey: #cfcfcf;
    --logo-grey: #8a8a8a;
  }
  * { box-sizing: border-box; margin: 0; padding: 0; }
  html, body { width: 1200px; height: 900px; overflow: hidden; }
  body {
    background: var(--page-bg);
    font-family: "Open Sans", Arial, sans-serif;
    display: flex;
    align-items: center;
    justify-content: center;
    gap: 40px;
  }
  .card {
    position: relative;
    width: 540px;
    height: 310px;
    background: var(--card-bg);
    border-radius: 22px;
    box-shadow: 0 2px 0 #d7d7d7, 0 5px 0 #c9c9c9, 0 14px 30px rgba(0,0,0,0.12);
    overflow: hidden;
  }
  .card-front { display: flex; align-items: center; justify-content: center; }
  .wordmark {
    display: flex;
    align-items: center;
    gap: 12px;
  }
  .wordmark-dot {
    width: 16px; height: 16px;
    border-radius: 50%;
    background: var(--brand-orange);
  }
  .wordmark-name {
    font-weight: 600;
    color: var(--brand-blue);
    font-size: 30px;
    letter-spacing: 0.2px;
  }
  .card-back .wordmark {
    position: absolute;
    top: 46px;
    left: 34px;
    gap: 7px;
  }
  .card-back .wordmark-dot { width: 9px; height: 9px; }
  .card-back .wordmark-name { font-size: 15px; }
  .divider {
    position: absolute;
    inset: 0;
  }
  .contact {
    position: absolute;
    left: 250px;
    top: 96px;
  }
  .contact-name {
    color: var(--brand-blue);
    font-size: 22px;
    font-weight: 400;
    line-height: 1.1;
  }
  .contact-role {
    color: var(--brand-orange);
    font-size: 19px;
    line-height: 1.2;
    margin-bottom: 12px;
  }
  .contact-details {
    list-style: none;
    color: var(--text-grey);
    font-size: 13px;
    line-height: 1.6;
  }
</style>
</head>
<body>
  <section class="card card-front" aria-label="Card front">
    <div class="wordmark">
      <span class="wordmark-dot"></span>
      <span class="wordmark-name">Vantor Plumbing &amp; Gas</span>
    </div>
  </section>

  <section class="card card-back" aria-label="Card back">
    <div class="wordmark">
      <span class="wordmark-dot"></span>
      <span class="wordmark-name">Vantor Plumbing &amp; Gas</span>
    </div>
    <svg class="divider" width="540" height="310" viewBox="0 0 540 310" aria-hidden="true">
      <defs>
        <linearGradient id="rule-fade" x1="0" y1="0" x2="0" y2="1">
          <stop offset="0" stop-color="#cfcfcf" stop-opacity="0"/>
          <stop offset="0.3" stop-color="#cfcfcf"/>
          <stop offset="0.8" stop-color="#cfcfcf"/>
          <stop offset="1" stop-color="#cfcfcf" stop-opacity="0"/>
        </linearGradient>
      </defs>
      <line x1="262" y1="40" x2="196" y2="270" stroke="url(#rule-fade)" stroke-width="1.2"/>
    </svg>
    <div class="contact">
      <h1 class="contact-name">Warren Dohey</h1>
      <p class="contact-role">Director</p>
      <ul class="contact-details">
        <li>Phone:-027 581 9043</li>
        <li>Mail:-warren@vantorplumbingandgas.example</li>
        <li>PO Box 7816</li>
        <li>Palmerston North 4472</li>
      </ul>
    </div>
  </section>
</body>
</html>
```